Velmar Intergrated Marketing Stationary Design Contest

We require a very professional looking stationary set to include: letterhead, compliments slip and business cards (double sided bus cards).

Files should be supplied on either Illustrator or InDesign.

We are interested in perhaps encorporating a faint watermark with the letter q or the logo, but it isnt a pre-requisite

Target Market(s)

Business owners seeking professional marketing services

Industry/Entity Type

Marketing

Requirements
Must have
• Concurrent theme wiht business cards, letterhead and comp slip. Must be an editable document for future ammendment
Should not have
• No use of times new roman or similar fonts

```html
<!DOCTYPE html>
<html lang="en">
<head>
<meta charset="utf-8">
<title>Velmar Integrated Marketing – Stationery Set</title>
<link href="https://fonts.googleapis.com/css2?family=Inter:ital,wght@0,300;0,400;1,300&display=swap" rel="stylesheet">
<style>
  :root {
    --brand-orange: #f15a2b;
    --wash-orange: #fdf3ef;
    --card-wash: #f3703f;
    --ink: #1a1a1a;
    --crop: #555555;
    --paper: #ffffff;
  }
  * { margin: 0; padding: 0; box-sizing: border-box; }
  html, body { width: 1200px; height: 869px; overflow: hidden; background: var(--paper); }
  body { position: relative; font-family: "Inter", Arial, sans-serif; font-weight: 300; color: var(--ink); }
  .crop-marks, .watermark { position: absolute; left: 0; top: 0; }
  .crop-marks line { stroke: var(--crop); stroke-width: 0.6; }
  .t { position: absolute; line-height: 1; white-space: nowrap; }
  .brand-name { font-weight: 300; letter-spacing: 0.12em; color: var(--ink); }
  .brand-dot { position: absolute; border-radius: 50%; background: var(--brand-orange); }
  .tagline { letter-spacing: 0.16em; }
  .italic { font-style: italic; }
  .business-card-back { position: absolute; left: 781px; top: 615px; width: 228px; height: 144px; background: var(--brand-orange); overflow: hidden; }
  .business-card-back .card-wash { position: absolute; left: 14px; top: 44px; width: 86px; height: 86px; border-radius: 50%; background: var(--card-wash); }
  .business-card-back .card-web { position: absolute; left: 104px; top: 67px; font-size: 7.5px; color: var(--paper); line-height: 1; }
</style>
</head>
<body>

<svg class="watermark" width="1200" height="869" aria-hidden="true">
  <circle cx="263" cy="581" r="145" fill="var(--wash-orange)"/>
  <circle cx="741" cy="278" r="83" fill="var(--wash-orange)"/>
</svg>

<svg class="crop-marks" width="1200" height="869" aria-hidden="true">
  <!-- letterhead -->
  <line x1="85.5" y1="50" x2="85.5" y2="79"/><line x1="53" y1="81" x2="81" y2="81"/>
  <line x1="582" y1="50" x2="582" y2="79"/><line x1="586" y1="81" x2="614" y2="81"/>
  <line x1="85.5" y1="790" x2="85.5" y2="818"/><line x1="53" y1="784" x2="81" y2="784"/>
  <line x1="582" y1="790" x2="582" y2="818"/><line x1="586" y1="784" x2="614" y2="784"/>
  <!-- compliments slip -->
  <line x1="639" y1="108" x2="639" y2="136"/><line x1="606" y1="140" x2="635" y2="140"/>
  <line x1="1136" y1="108" x2="1136" y2="136"/><line x1="1141" y1="140" x2="1169" y2="140"/>
  <line x1="639" y1="382" x2="639" y2="410"/><line x1="606" y1="376" x2="635" y2="376"/>
  <line x1="1136" y1="382" x2="1136" y2="410"/><line x1="1141" y1="376" x2="1169" y2="376"/>
  <!-- business card -->
  <line x1="788" y1="447" x2="788" y2="475"/><line x1="756" y1="479" x2="784" y2="479"/>
  <line x1="1001" y1="447" x2="1001" y2="475"/><line x1="1006" y1="479" x2="1034" y2="479"/>
  <line x1="756" y1="610" x2="784" y2="610"/><line x1="1006" y1="610" x2="1034" y2="610"/>
  <line x1="756" y1="621" x2="784" y2="621"/><line x1="1006" y1="621" x2="1034" y2="621"/>
  <line x1="756" y1="751" x2="784" y2="751"/><line x1="1006" y1="751" x2="1034" y2="751"/>
  <line x1="788" y1="759" x2="788" y2="785"/><line x1="1001" y1="759" x2="1001" y2="785"/>
</svg>

<!-- Letterhead -->
<section class="letterhead">
  <span class="brand-dot" style="left:388px;top:128px;width:40px;height:40px;"></span>
  <div class="t brand-name" style="left:433px;top:124px;font-size:32px;">velmar</div>
  <div class="t tagline" style="left:433px;top:157px;font-size:8.5px;">Integrated Marketing</div>
  <div class="t" style="left:433px;top:180px;font-size:8.5px;">Harbour House</div>
  <div class="t" style="left:433px;top:195px;font-size:8.5px;">Kestrel Row</div>
  <div class="t" style="left:433px;top:210px;font-size:8.5px;">Ashbridge</div>
  <div class="t" style="left:433px;top:225px;font-size:8.5px;">Calder Vale</div>
  <div class="t" style="left:433px;top:240px;font-size:8.5px;">HX9 4QT</div>
  <div class="t" style="left:433px;top:270px;font-size:8.5px;">Web</div>
  <div class="t" style="left:467px;top:270px;font-size:8.5px;">www.velmarim.co.uk</div>
  <div class="t" style="left:433px;top:285px;font-size:8.5px;">Email</div>
  <div class="t" style="left:467px;top:285px;font-size:8.5px;">enquiries@velmarim.co.uk</div>
  <div class="t" style="left:433px;top:300px;font-size:8.5px;">Tel</div>
  <div class="t" style="left:467px;top:300px;font-size:8.5px;">01632 960614</div>
  <div class="t" style="left:433px;top:315px;font-size:8.5px;">Fax</div>
  <div class="t" style="left:467px;top:315px;font-size:8.5px;">01632 960611</div>
  <div class="t italic" style="left:433px;top:734px;font-size:7.5px;">Company registration &nbsp; 4815162</div>
  <div class="t italic" style="left:433px;top:746px;font-size:7.5px;">Vat No &nbsp; 712 4408 51</div>
  <div class="t italic" style="left:433px;top:759px;font-size:7.5px;">Trading as a division of Brantley Ltd</div>
</section>

<!-- Compliments slip -->
<section class="compliments-slip">
  <div class="t" style="left:661px;top:166px;font-size:13px;font-weight:400;">with compliments</div>
  <span class="brand-dot" style="left:943px;top:169px;width:40px;height:40px;"></span>
  <div class="t brand-name" style="left:988px;top:165px;font-size:32px;">velmar</div>
  <div class="t tagline" style="left:988px;top:198px;font-size:8.5px;">Integrated Marketing</div>
  <div class="t" style="left:988px;top:220px;font-size:8.5px;">Harbour House</div>
  <div class="t" style="left:988px;top:236px;font-size:8.5px;">Kestrel Row</div>
  <div class="t" style="left:988px;top:251px;font-size:8.5px;">Ashbridge</div>
  <div class="t" style="left:988px;top:266px;font-size:8.5px;">Calder Vale</div>
  <div class="t" style="left:988px;top:281px;font-size:8.5px;">HX9 4QT</div>
  <div class="t" style="left:988px;top:311px;font-size:8.5px;">Web</div>
  <div class="t" style="left:1022px;top:311px;font-size:8.5px;">www.velmarim.co.uk</div>
  <div class="t" style="left:988px;top:326px;font-size:8.5px;">Email</div>
  <div class="t" style="left:1022px;top:326px;font-size:8.5px;">enquiries@velmarim.co.uk</div>
  <div class="t" style="left:988px;top:341px;font-size:8.5px;">Tel</div>
  <div class="t" style="left:1022px;top:341px;font-size:8.5px;">01632 960614</div>
  <div class="t" style="left:988px;top:356px;font-size:8.5px;">Fax</div>
  <div class="t" style="left:1022px;top:356px;font-size:8.5px;">01632 960611</div>
  <div class="t italic" style="left:659px;top:331px;font-size:7.5px;">Company registration &nbsp; 4815162</div>
  <div class="t italic" style="left:659px;top:344px;font-size:7.5px;">Vat No &nbsp; 712 4408 51</div>
  <div class="t italic" style="left:659px;top:356px;font-size:7.5px;">Trading as a division of Brantley Ltd</div>
</section>

<!-- Business card front -->
<section class="business-card-front">
  <span class="brand-dot" style="left:846px;top:490px;width:34px;height:34px;"></span>
  <div class="t brand-name" style="left:884px;top:492px;font-size:24px;">velmar</div>
  <div class="t tagline" style="left:884px;top:515px;font-size:6.5px;">Integrated Marketing</div>
  <div class="t" style="left:885px;top:533px;font-size:6.5px;">Harbour House</div>
  <div class="t" style="left:885px;top:543px;font-size:6.5px;">Kestrel Row, Ashbridge</div>
  <div class="t" style="left:885px;top:553px;font-size:6.5px;">Calder Vale &nbsp;HX9 4QT</div>
  <div class="t" style="left:807px;top:559px;font-size:8.5px;font-weight:400;">Owen Hartley</div>
  <div class="t italic" style="left:808px;top:569px;font-size:6px;">General Manager</div>
  <div class="t" style="left:885px;top:573px;font-size:6.5px;">Email</div>
  <div class="t" style="left:909px;top:573px;font-size:6.5px;">enquiries@velmarim.co.uk</div>
  <div class="t" style="left:885px;top:583px;font-size:6.5px;">Tel</div>
  <div class="t" style="left:909px;top:583px;font-size:6.5px;">01632 960614</div>
  <div class="t" style="left:885px;top:593px;font-size:6.5px;">Fax</div>
  <div class="t" style="left:909px;top:593px;font-size:6.5px;">01632 960611</div>
</section>

<!-- Business card back -->
<section class="business-card-back">
  <span class="card-wash" aria-hidden="true"></span>
  <div class="card-web">www.velmarim.co.uk</div>
</section>

</body>
</html>
```